New Company Business Card Design

I have a new company logo and I want a new business card design. I dont know if the logo file i attached is in the correct format or quality. We are a New York City Specialty construction Firm specializing in high risk out of the box projects. I want a simple and classy business card that people will his card is as crisp as the work his company does.

Target Market(s)

Clients in the heavy construction industry in New York City

Industry/Entity Type

Construction Company

Contact Information for Business Card

Simple Classy - DIFFERENT

Font styles to use
Other font styles liked:
• Mach the logo font in some way

Colors

Designer to choose colors to be used in the design.

Requirements
Must have
• Uniqueness
Nice to have
• Nothing particular - Just different and classy - Timeless
Should not have
• Goofy Shit or Gimmicky shit

```html
<!DOCTYPE html>
<html lang="en">
<head>
<meta charset="utf-8">
<title>KRT Builders — Business Card</title>
<link rel="stylesheet" href="https://fonts.googleapis.com/css2?family=Arimo:wght@400;700&display=swap">
<style>
  :root {
    --stage: #2b2b2b;
    --paper: #ffffff;
    --paper-shade: #ececec;
    --brand-blue: #0f57a6;
    --brand-blue-deep: #0a3f80;
    --swoosh: #151515;
    --on-blue: #dfe9f6;
    --on-blue-soft: #b9cde6;
  }
  * { box-sizing: border-box; margin: 0; padding: 0; }
  html, body { width: 1200px; height: 997px; overflow: hidden; }
  body {
    background: var(--stage);
    font-family: "Arimo", Arial, sans-serif;
    position: relative;
  }
  .card {
    position: absolute;
    left: 250px;
    width: 700px;
    height: 400px;
    background: linear-gradient(160deg, var(--paper) 40%, var(--paper-shade));
    overflow: hidden;
    box-shadow: 0 10px 30px rgba(0,0,0,.5);
  }
  .card--back { top: 60px; }
  .card--front { top: 537px; }
  .card__art { position: absolute; inset: 0; width: 100%; height: 100%; }
  .card__brand {
    position: absolute;
    color: var(--brand-blue);
    font-weight: 700;
    letter-spacing: .02em;
    white-space: nowrap;
  }
  .card--back .card__brand {
    top: 70px; left: 0; width: 560px; text-align: center;
    font-size: 120px; line-height: 1;
  }
  .card--front .card__brand {
    top: 80px; left: 0; width: 700px; text-align: center;
    font-size: 44px; line-height: 1;
  }
  .website {
    font-size: 15px;
    letter-spacing: .35em;
    fill: var(--on-blue);
    font-weight: 700;
  }
  .holder {
    position: absolute;
    left: 120px; top: 300px;
    width: 230px;
    text-align: right;
    color: var(--on-blue);
  }
  .holder__name { font-weight: 700; font-size: 19px; letter-spacing: .02em; }
  .holder__role { font-size: 16px; color: var(--on-blue-soft); margin-top: 2px; }
  .divider {
    position: absolute; left: 380px; top: 262px;
    width: 1px; height: 110px;
    background: var(--on-blue-soft);
  }
  .contacts {
    position: absolute; left: 405px; top: 262px;
    list-style: none;
    color: var(--on-blue);
    font-size: 16px;
  }
  .contacts__item { display: flex; align-items: center; gap: 14px; height: 34px; }
  .contacts__icon { width: 18px; height: 18px; flex: none; }
</style>
</head>
<body>

<section class="card card--back" aria-label="Card back">
  <svg class="card__art" viewBox="0 0 700 400" aria-hidden="true">
    <defs>
      <linearGradient id="blueBack" x1="0" y1="0" x2="1" y2="1">
        <stop offset="0" stop-color="#1a6cc0"/>
        <stop offset="1" stop-color="#0a3f80"/>
      </linearGradient>
      <path id="sitePath" d="M150,385 Q380,190 690,150"/>
    </defs>
    <path d="M0,400 L0,395 Q330,170 700,115 L700,400 Z" fill="url(#blueBack)"/>
    <path d="M40,400 Q330,140 700,95 Q330,160 70,400 Z" fill="var(--swoosh)"/>
    <text class="website"><textPath href="#sitePath" startOffset="12%">www.krtbuilders.com</textPath></text>
  </svg>
  <div class="card__brand">KRT</div>
</section>

<section class="card card--front" aria-label="Card front">
  <svg class="card__art" viewBox="0 0 700 400" aria-hidden="true">
    <defs>
      <linearGradient id="blueFront" x1="0" y1="0" x2="1" y2="1">
        <stop offset="0" stop-color="#1462b3"/>
        <stop offset="1" stop-color="#0a3f80"/>
      </linearGradient>
    </defs>
    <path d="M0,400 L0,330 Q280,170 700,175 L700,400 Z" fill="url(#blueFront)"/>
    <path d="M60,370 Q300,150 690,150 Q300,170 80,370 Z" fill="var(--swoosh)"/>
  </svg>

  <div class="card__brand">KRT Builders, Inc.</div>

  <div class="holder">
    <p class="holder__name">LARS EMDEN</p>
    <p class="holder__role">Director</p>
  </div>

  <div class="divider"></div>

  <ul class="contacts">
    <li class="contacts__item">
      <svg class="contacts__icon" viewBox="0 0 18 18" aria-hidden="true">
        <circle cx="9" cy="9" r="9" fill="#dfe9f6"/>
        <path d="M5,7 Q9,4 13,7 L12,8.5 L10.5,7.8 L7.5,7.8 L6,8.5 Z M6,10 H12 V13 H6 Z" fill="#0a3f80"/>
      </svg>
      <span>555 010 2230</span>
    </li>
    <li class="contacts__item">
      <svg class="contacts__icon" viewBox="0 0 18 18" aria-hidden="true">
        <circle cx="9" cy="9" r="9" fill="#dfe9f6"/>
        <rect x="6" y="4" width="6" height="10" rx="1" fill="#0a3f80"/>
        <rect x="7" y="5.5" width="4" height="6" fill="#dfe9f6"/>
      </svg>
      <span>555 010 4478</span>
    </li>
    <li class="contacts__item">
      <svg class="contacts__icon" viewBox="0 0 18 18" aria-hidden="true">
        <circle cx="9" cy="9" r="9" fill="#dfe9f6"/>
        <rect x="4.5" y="6" width="9" height="6.5" fill="#0a3f80"/>
        <path d="M4.5,6 L9,9.5 L13.5,6" fill="none" stroke="#dfe9f6" stroke-width="1"/>
      </svg>
      <span>lars@krtbuilders.com</span>
    </li>
  </ul>
</section>

</body>
</html>
```